Clone https://brinwexo.com (fully functional wordpress site with wooCommerce)

1) Clone or recreate the site in WordPress Woocomerece
2) Connect to our existing stripe account.
3) Make our text only changes (not style changes or anything complex.

We will provide all graphics and content to be copied and pasted in place of the existing text / graphics.

Please do not submit a design only. Thanks in advance.

Target Market(s)

Wordpress developer

Number of Pages Required

5+ page

Font styles to use
Sans Serif

Colors
acd036
9bcb3c
cadf82
eaf2ce

Requirements
Must have
• Fully functional wordpress site with Woo Comerece pluged in.
Should not have
• Design only

```html
<!DOCTYPE html>
<html lang="en">
<head>
<meta charset="utf-8">
<title>Veranto – 24/7 Live Answering Service</title>
<link href="https://fonts.googleapis.com/css2?family=Roboto:wght@300;400;500;700&display=swap" rel="stylesheet">
<style>
:root{
  --green:#8bc53f;
  --green-dark:#79b22f;
  --green-soft:#cadf82;
  --green-pale:#eaf2ce;
  --ink:#2b2b2b;
  --muted:#5c5c5c;
  --grey-bg:#f4f4f4;
  --line:#e4e4e4;
  --footer:#323436;
  --white:#ffffff;
}
*{box-sizing:border-box;margin:0;padding:0}
html,body{width:1200px;height:4063px;overflow:hidden}
body{font-family:'Roboto',Arial,sans-serif;color:var(--ink);background:var(--white);position:relative}
.abs{position:absolute}
p{line-height:1.5}

/* hero */
.hero{position:absolute;left:0;top:0;width:1200px;height:610px;background:linear-gradient(135deg,#3d4043 0%,#2c2e30 55%,#3a3c3e 100%)}
.hero-photo{position:absolute;inset:0;background:radial-gradient(ellipse at 75% 60%,rgba(120,124,128,.35),transparent 60%)}
.nav{position:absolute;left:87px;right:90px;top:30px;height:80px;display:flex;align-items:center}
.brand{display:flex;align-items:center;gap:12px;color:var(--white);font-size:20px;font-weight:500}
.brand-dot{width:22px;height:22px;border-radius:50%;background:var(--white)}
.nav-phone{color:var(--white);font-size:17px;margin-left:36px;letter-spacing:1px}
.nav-links{margin-left:auto;display:flex;align-items:center;gap:26px}
.nav-links a{color:var(--white);font-size:11px;text-decoration:none;text-transform:uppercase;letter-spacing:.5px}
.btn-login{background:var(--green);padding:8px 16px}
.btn-trial{border:1px solid var(--white);padding:7px 14px}
.hero-title{position:absolute;top:258px;left:0;width:1200px;text-align:center;color:var(--white);font-size:42px;font-weight:400}
.hero-sub{position:absolute;top:318px;left:350px;width:500px;text-align:center;color:var(--white);font-size:14px;font-weight:500}
.hero-cta{position:absolute;top:373px;left:513px;width:174px;height:42px;border:1px solid var(--green);color:var(--white);font-size:11px;font-weight:500;display:flex;align-items:center;justify-content:center;text-transform:uppercase;letter-spacing:.5px}

/* shared section title */
.section-title{position:absolute;text-align:center;font-size:34px;font-weight:400;color:var(--ink)}
.title-rule{position:absolute;left:0;width:1200px;height:1px;background:var(--line)}

/* teams */
.teams{position:absolute;top:610px;left:0;width:1200px;height:479px;background:var(--white)}
.team-card{position:absolute;width:260px;text-align:center}
.team-photo{width:108px;height:108px;border-radius:50%;margin:0 auto 14px;background:linear-gradient(160deg,#c9c9c9,#8c8c8c);border:4px solid #eeeeee}
.team-name{color:var(--green);font-size:14px}
.team-role{font-size:12px;margin-top:2px}
.team-quote{font-size:11px;color:var(--muted);margin-top:10px;line-height:1.45}
.arrow{position:absolute;top:282px}

/* message taking */
.messages{position:absolute;top:1089px;left:0;width:1200px;height:964px;background:var(--grey-bg)}
.feature{position:absolute;width:260px;text-align:center}
.feature svg{display:block;margin:0 auto 8px}
.feature h4{font-size:12px;font-weight:400;margin-bottom:4px}
.feature p{font-size:11px;color:var(--muted);line-height:1.45}
.phone-hand{position:absolute;left:423px;top:333px;width:363px;height:631px;background:linear-gradient(180deg,#3d4448 0%,#2a2e31 55%,#d9c2b0 80%,#e6d2c2 100%);border-radius:40px 40px 0 0}
.btn-services{position:absolute;left:415px;top:856px;width:371px;height:46px;background:var(--green);color:var(--white);font-size:11px;font-weight:500;display:flex;align-items:center;justify-content:center;text-transform:uppercase;letter-spacing:.5px}

/* languages */
.languages{position:absolute;top:2053px;left:0;width:1200px;height:420px}
.lang h2{font-size:56px;color:var(--green);font-weight:700;line-height:1}
.lang h3{font-size:30px;font-weight:400;margin:10px 0 14px}
.lang p{font-size:13px;color:var(--muted);line-height:1.6}
.greeting-art{position:absolute;left:447px;top:150px;width:290px;height:190px;border-radius:90px;background:radial-gradient(ellipse at center,var(--green-pale) 0%,#f6f9ec 60%,var(--white) 100%)}

/* service */
.service-tabs{position:absolute;top:2567px;left:290px;display:flex;font-size:12px}
.service-tabs span{padding:12px 18px}
.service-tabs .active{background:var(--green);color:var(--white)}
.service-band{position:absolute;top:2609px;left:0;width:1200px;height:295px;background:var(--green)}
.agent{position:absolute;left:182px;top:40px;width:140px;text-align:center;color:var(--white);font-size:11px;line-height:1.5}
.agent-photo{width:108px;height:108px;border-radius:50%;margin:0 auto 16px;background:linear-gradient(160deg,#d8d8d8,#7f7f7f);border:4px solid var(--white)}
.waveform{position:absolute;left:420px;top:78px;width:596px;height:70px;background:repeating-linear-gradient(90deg,rgba(60,110,20,.55) 0 3px,transparent 3px 6px);clip-path:polygon(0 50%,8% 30%,15% 45%,22% 10%,30% 40%,38% 20%,46% 0,55% 35%,63% 15%,72% 45%,80% 25%,90% 40%,100% 50%,90% 60%,80% 75%,72% 55%,63% 85%,55% 65%,46% 100%,38% 80%,30% 60%,22% 90%,15% 55%,8% 70%)}
.play{position:absolute;left:374px;top:98px;width:30px;height:30px;border-radius:50%;background:var(--white);display:flex;align-items:center;justify-content:center}
.service-text{position:absolute;left:382px;top:176px;width:715px;color:var(--white);font-size:12px;line-height:1.6}

/* stats */
.stat{position:absolute;top:2995px;width:330px}
.stat h5{font-size:22px;font-weight:400}
.stat-num{font-size:120px;color:var(--green);font-weight:300;line-height:1;display:inline-block;vertical-align:top;margin-top:4px}
.stat p{display:inline-block;width:170px;margin:28px 0 0 24px;font-size:12px;color:var(--muted);vertical-align:top}

/* demo */
.demo{position:absolute;top:3218px;left:0;width:1200px;height:480px}
.demo-photo{position:absolute;inset:0;background:linear-gradient(120deg,#2c2e30 0%,#37393b 60%,#454749 100%)}
.demo h2{position:absolute;top:86px;left:0;width:1200px;text-align:center;color:var(--white);font-size:34px;font-weight:400}
.demo-sub{position:absolute;top:136px;left:0;width:1200px;text-align:center;color:var(--white);font-size:12px;font-weight:500}
.field{position:absolute;left:447px;width:306px;height:38px;background:var(--white);font-size:11px;color:var(--muted);padding:0 12px;display:flex;align-items:center}
.btn-demo{position:absolute;left:447px;top:380px;width:306px;height:42px;background:#4b5a3a;border:1px solid var(--green);color:var(--white);font-size:11px;display:flex;align-items:center;justify-content:center;text-transform:uppercase}

/* footer */
.footer{position:absolute;top:3698px;left:0;width:1200px;height:325px;background:var(--footer)}
.footer-art{position:absolute;left:122px;top:54px;width:271px;height:230px;border-radius:50%;background:radial-gradient(circle,rgba(139,197,63,.28),rgba(139,197,63,.06) 70%)}
.footer-col{position:absolute;top:108px;font-size:12px;color:#c9c9c9;line-height:27px}
.social{position:absolute;left:978px;top:178px;display:flex;gap:10px}
.social span{width:22px;height:22px;border-radius:50%;background:#4a4c4e}
.bottom-bar{position:absolute;top:4023px;left:0;width:1200px;height:40px;background:#2a2b2d;color:#aaa;font-size:11px;display:flex;align-items:center;padding-left:87px;gap:26px}
.chat{position:absolute;left:902px;top:3976px;display:flex;align-items:center;gap:10px}
.chat-bubble{background:var(--white);border-radius:10px;padding:10px 14px;font-size:12px;color:var(--ink);width:180px;line-height:1.4;box-shadow:0 2px 8px rgba(0,0,0,.25)}
.chat-btn{width:62px;height:62px;border-radius:50%;background:var(--green);display:flex;align-items:center;justify-content:center}
</style>
</head>
<body>

<header class="hero">
  <div class="hero-photo" role="img" aria-label="Dark photo of a desk with a telephone and headset"></div>
  <nav class="nav">
    <div class="brand"><span class="brand-dot"></span>Veranto</div>
    <div class="nav-phone">(125) 4680 31</div>
    <div class="nav-links">
      <a href="#">Services</a><a href="#">Customers</a><a href="#">Pricing</a><a href="#">Contact Us</a>
      <a href="#" class="btn-login">Login</a><a href="#" class="btn-trial">Free Trial</a>
    </div>
  </nav>
  <h1 class="hero-title">24/7 Live Answering Service</h1>
  <p class="hero-sub">Lorem ipsum dolor sit amet, consectetuer adipiscing elit. Aenean commodo cum sociis natoque penatibus et magnis</p>
  <div class="hero-cta">Start a Free Trial</div>
</header>

<section class="teams">
  <div class="title-rule" style="top:113px"></div>
  <h2 class="section-title" style="top:88px;background:var(--white);width:260px;left:470px">Our Teams</h2>
  <svg class="arrow" style="left:88px" width="16" height="26" viewBox="0 0 16 26"><path d="M13 2 3 13l10 11" fill="none" stroke="#333" stroke-width="2.5"/></svg>
  <svg class="arrow" style="left:1096px" width="16" height="26" viewBox="0 0 16 26"><path d="M3 2l10 11L3 24" fill="none" stroke="#333" stroke-width="2.5"/></svg>
  <div class="team-card" style="left:133px;top:180px">
    <div class="team-photo" role="img" aria-label="Portrait photo of team lead"></div>
    <div class="team-name">John Smith</div><div class="team-role">Team Lead</div>
    <p class="team-quote">"Lorem ipsum dolor sit amet, cing elit. Aenean commodo ligula eget dolor aenean massa cum sociis"</p>
  </div>
  <div class="team-card" style="left:471px;top:180px">
    <div class="team-photo" role="img" aria-label="Portrait photo of team lead"></div>
    <div class="team-name">John Smith</div><div class="team-role">Team Lead</div>
    <p class="team-quote">"Lorem ipsum dolor sit amet, cing elit. Aenean commodo ligula eget dolor aenean massa cum sociis"</p>
  </div>
  <div class="team-card" style="left:810px;top:180px">
    <div class="team-photo" role="img" aria-label="Portrait photo of team lead"></div>
    <div class="team-name">John Smith</div><div class="team-role">Team Lead</div>
    <p class="team-quote">"Lorem ipsum dolor sit amet, cing elit. Aenean commodo ligula eget dolor aenean massa cum sociis"</p>
  </div>
</section>

<section class="messages">
  <div class="title-rule" style="top:93px"></div>
  <h2 class="section-title" style="top:68px;background:var(--grey-bg);width:400px;left:400px">Just message taking</h2>

  <div class="feature" style="left:176px;top:164px"><svg width="36" height="30"><rect x="3" y="10" width="30" height="16" rx="2" fill="none" stroke="#8bc53f" stroke-width="2"/></svg><h4>Heading 1</h4><p>Lorem ipsum dolor sit amet cing elit aenean modo ligula eget dolor aenean.</p></div>
  <div class="feature" style="left:471px;top:164px"><svg width="36" height="30"><rect x="8" y="3" width="20" height="24" rx="2" fill="none" stroke="#8bc53f" stroke-width="2"/></svg><h4>Heading 2</h4><p>Lorem ipsum dolor sit amet cing elit aenean modo ligula eget dolor aenean.</p></div>
  <div class="feature" style="left:810px;top:164px"><svg width="36" height="30"><rect x="5" y="5" width="26" height="22" rx="2" fill="none" stroke="#8bc53f" stroke-width="2"/><path d="M5 12h26" stroke="#8bc53f" stroke-width="2"/></svg><h4>Heading 3</h4><p>Lorem ipsum dolor sit amet cing elit aenean modo ligula eget dolor aenean.</p></div>

  <div class="feature" style="left:176px;top:352px"><svg width="36" height="30"><rect x="4" y="5" width="28" height="20" rx="2" fill="none" stroke="#8bc53f" stroke-width="2"/></svg><h4>Heading 4</h4><p>Lorem ipsum dolor sit amet cing elit aenean modo ligula eget dolor aenean.</p></div>
  <div class="feature" style="left:810px;top:352px"><svg width="36" height="30"><path d="M5 6l9 4 9-4 8 4v16l-8-4-9 4-9-4z" fill="none" stroke="#8bc53f" stroke-width="2"/></svg><h4>Heading 5</h4><p>Lorem ipsum dolor sit amet cing elit aenean modo ligula eget dolor aenean.</p></div>

  <div class="feature" style="left:176px;top:540px"><svg width="36" height="30"><rect x="3" y="6" width="28" height="18" rx="2" fill="none" stroke="#8bc53f" stroke-width="2"/><path d="M3 12h28" stroke="#8bc53f" stroke-width="2"/></svg><h4>Heading 6</h4><p>Lorem ipsum dolor sit amet cing elit aenean modo ligula eget dolor aenean.</p></div>
  <div class="feature" style="left:810px;top:540px"><svg width="36" height="30"><circle cx="10" cy="12" r="5" fill="none" stroke="#8bc53f" stroke-width="2"/><circle cx="26" cy="12" r="5" fill="none" stroke="#8bc53f" stroke-width="2"/><circle cx="18" cy="20" r="5" fill="none" stroke="#8bc53f" stroke-width="2"/></svg><h4>Heading 7</h4><p>Lorem ipsum dolor sit amet cing elit aenean modo ligula eget dolor aenean.</p></div>

  <div class="feature" style="left:176px;top:718px"><svg width="36" height="30"><path d="M22 4a11 11 0 1 0 9 15A9 9 0 0 1 22 4z" fill="none" stroke="#8bc53f" stroke-width="2"/></svg><h4>Heading 8</h4><p>Lorem ipsum dolor sit amet cing elit aenean modo ligula eget dolor aenean.</p></div>
  <div class="feature" style="left:810px;top:718px"><svg width="36" height="30"><path d="M9 4l5 6-3 3c2 4 5 7 9 9l3-3 6 5-3 4C15 27 8 20 6 7z" fill="none" stroke="#8bc53f" stroke-width="2"/></svg><h4>Heading 9</h4><p>Lorem ipsum dolor sit amet cing elit aenean modo ligula eget dolor aenean.</p></div>

  <div class="phone-hand" role="img" aria-label="Photo of a hand holding a smartphone showing the app screen"></div>
  <div class="btn-services">Learn more about our answer services</div>
</section>

<section class="languages">
  <div class="lang abs" style="left:87px;top:118px;width:346px">
    <h2>English</h2><h3>24/7 Coverage</h3>
    <p>Lorem ipsum dolor sit amet, consectetuer adipiscing elit. Aenean commodo ligula eget dolor aenean massa. Cum sociis natoque penatibus et magnis dis parturient montes, nascetur ridiculus mus. Donec quam felis, ultricies nec, pellentesque eu, pretium quis, sem. Nulla consequat massa quis enim donec pede justo.</p>
  </div>
  <div class="greeting-art" role="img" aria-label="Illustration of two green speech bubbles saying hello and holá"></div>
  <div class="lang abs" style="left:777px;top:118px;width:333px">
    <h2>Spanish</h2><h3>7am to Midnight</h3>
    <p>Lorem ipsum dolor sit amet, consectetuer adipiscing elit. Aenean commodo ligula eget dolor aenean massa. Cum sociis natoque penatibus et magnis dis parturient montes, nascetur ridiculus mus. Donec quam felis, ultricies nec, pellentesque eu, pretium quis, sem. Nulla consequat massa quis enim donec pede justo.</p>
  </div>
</section>

<div class="title-rule" style="top:2518px"></div>
<h2 class="section-title" style="top:2494px;background:var(--white);width:420px;left:390px">Service on every call</h2>
<div class="service-tabs">
  <span class="active">Message Taking</span><span>Lead Collection</span><span>Appointment Scheduling</span><span>Order Processing</span>
</div>
<section class="service-band">
  <div class="agent">
    <div class="agent-photo" role="img" aria-label="Portrait photo of live receptionist"></div>
    JOHN SMITH<br>Live Receptionist<br>Team Member Since 2017
  </div>
  <div class="play"><svg width="12" height="14"><path d="M2 1l9 6-9 6z" fill="#8bc53f"/></svg></div>
  <div class="waveform" role="img" aria-label="Audio waveform of a recorded call"></div>
  <p class="service-text">Lorem ipsum dolor sit amet, consectetuer adipiscing elit. Aenean commodo ligula eget dolor. Aenean massa. Cum sociis natoque penatibus et magnis dis parturient montes, nascetur ridiculus mus. Donec quam felis, ultricies nec, pellentesque eu, pretium quis, sem. Nulla consequat massa quis enim. Donec pede justo, fri.</p>
</section>

<section>
  <div class="stat" style="left:87px"><h5>Experienced</h5><span class="stat-num">27</span><p>Lorem ipsum dolor sit amet, consectetuer adipiscing elit. Aenean commodo ligula eget dolo aenean massa.</p></div>
  <div class="stat" style="left:469px"><h5>Accomplished</h5><span class="stat-num">3</span><p>Lorem ipsum dolor sit amet, consectetuer adipiscing elit. Aenean commodo ligula eget dolo aenean massa.</p></div>
  <div class="stat" style="left:786px"><h5>Consistent</h5><span class="stat-num">24</span><p>Lorem ipsum dolor sit amet, consectetuer adipiscing elit. Aenean commodo ligula eget dolo aenean massa.</p></div>
</section>

<section class="demo">
  <div class="demo-photo" role="img" aria-label="Dark photo of a person using a phone at a desk"></div>
  <h2>Request a Demo</h2>
  <p class="demo-sub">Lorem ipsum dolor sit amet, consectetuer adipiscing elit. aenean commodo</p>
  <div class="field" style="top:201px">Name*</div>
  <div class="field" style="top:245px">Email Address*</div>
  <div class="field" style="top:290px">Phone Number*</div>
  <div class="field" style="top:334px">How did you hear about Us*</div>
  <div class="btn-demo">Request a Sales Demo</div>
</section>

<footer class="footer">
  <div class="footer-art" role="img" aria-label="Line illustration of a telephone surrounded by service icons"></div>
  <div class="footer-col" style="left:536px">Services<br>Customers<br>Pricing<br>FAQ</div>
  <div class="footer-col" style="left:756px">Blog<br>About<br>Careers<br>Contact Us</div>
  <div class="footer-col" style="left:978px;top:100px">Sales@example.com<br>Support@example.com</div>
  <div class="social"><span></span><span></span><span></span></div>
</footer>
<div class="bottom-bar"><span>© 2017. All rights reserved.</span><span>Privacy Policy</span><span>Terms of Service</span></div>
<div class="chat">
  <div class="chat-bubble">Welcome back! Do you have any questions?</div>
  <div class="chat-btn"><svg width="28" height="26" viewBox="0 0 28 26"><path d="M4 3h20a2 2 0 0 1 2 2v12a2 2 0 0 1-2 2H12l-6 5v-5H4a2 2 0 0 1-2-2V5a2 2 0 0 1 2-2z" fill="#fff"/></svg></div>
</div>

</body>
</html>
```